New York City Sponsorship Page with Click Through Supporting Pages

Metro Workforce Guild, the leading New York City resource for HR Professionals is a membership organization with almost 2,000 individual members.

We need section/page(s) created for our current sponsorship offerings. Our platform is on ClubRoster Platform and we need capability to edit the page, etc. It must be HTML ready/coded.

Attached is the mock up of how we want the page to look (pages mockup pdf) as well as each of the categories which should be included (in the excel files). Our current page is here: http://www.metroworkguild.org/?page=sponsors and is not easy to read through. We want something that is visually appealing and clean but showcases all of the different ways to sponsor the Chapter.

Additionally, we are taking the information from this page and turning it into a brochure.

Target Market(s)

New York City Companies who have HR Professionals or services they want to attract or offer.

Coding

Coded - Design and coding required

Number of Pages Required

5+ page

Requirements
Must have
• Clean Look and feel, easy functionality, necessary information and purchases. Match the top navigation of current page. Opportunity for current sponsor logos to be highlighted on the page. Easy to update/maintain.
Nice to have
• Option to pay for sponsorships through the page using our credit card processor.
Should not have
• Overwhelming text in sections

```html
<!DOCTYPE html>
<html lang="en">
<head>
<meta charset="utf-8">
<title>Invitation for Strategic Partners – Metro Workforce Guild</title>
<link rel="stylesheet" href="https://fonts.googleapis.com/css2?family=Roboto+Condensed:wght@300;400;700&family=Arimo:wght@400;700&display=swap">
<style>
:root{
  --navy:#0a2240;
  --navy-deep:#071a33;
  --blue:#0b7dd3;
  --link:#1a86cc;
  --red:#a8321f;
  --red-link:#c0171d;
  --text:#1c1c1c;
  --muted:#555;
  --panel:#efefef;
  --header:#f0f0f0;
}
*{box-sizing:border-box;margin:0;padding:0}
html,body{width:1150px;height:1200px;overflow:hidden;background:#fff}
body{font-family:"Arimo",Arial,sans-serif;color:var(--text);position:relative}
.abs{position:absolute}

/* top bar */
.topbar{left:0;top:0;width:1150px;height:24px;background:var(--navy)}
.toplinks{right:403px;top:7px;display:flex;gap:9px;font-size:8px;line-height:10px;color:#fff;font-weight:700;white-space:nowrap}
.search{left:758px;top:5px;width:107px;height:14px;background:#fff;border-radius:2px;font-size:7.5px;color:#999;padding:3px 5px;white-space:nowrap}
.search svg{position:absolute;right:4px;top:3px}
.topsocial{left:872px;top:5px;display:flex;gap:4px}
.sq{width:16px;height:16px;background:var(--blue);display:block}

/* header */
.header{left:0;top:24px;width:1150px;height:58px;background:var(--header)}
.brand{left:184px;top:41px;display:flex;align-items:center;gap:6px;font-family:"Roboto Condensed",sans-serif;font-weight:700;font-size:16px;color:var(--red)}
.brand .dot{width:14px;height:14px;border-radius:50%;background:var(--navy)}
.nav{left:425px;top:46px;display:flex;gap:23px;font-family:"Roboto Condensed",sans-serif;font-size:12.5px;color:var(--link)}
.hero{left:0;top:82px;width:1150px;height:105px;background:linear-gradient(180deg,#1a2030 0%,#2b2c33 45%,#3a3225 75%,#111 100%)}

/* main */
.title{left:182px;top:215px;font-family:"Roboto Condensed",sans-serif;font-weight:300;font-size:27px;color:var(--red)}
.crumb{left:182px;top:259px;font-size:9px;color:#333}
.share{left:182px;top:286px;display:flex;align-items:center;gap:3px;font-family:"Roboto Condensed",sans-serif;font-size:10.5px;color:var(--red)}
.share .mini{width:11px;height:11px;display:inline-block}
.p{left:182px;font-size:10.5px}
.acc{left:182px;width:495px;height:28px;border-radius:3px;color:#fff;font-size:10.5px;padding:0 15px;display:flex;align-items:center;justify-content:space-between}
.acc.open{background:var(--blue)}
.acc.closed{background:var(--navy)}
.badge{left:186px;top:416px;width:64px;height:64px;border-radius:50%;background:#d9e2ea}
.benefits{left:192px;top:543px;list-style:none;font-size:10.5px;color:#444}
.benefits li{height:17.5px;display:flex;align-items:center;gap:8px}
.benefits li::before{content:"";border-left:5px solid #555;border-top:3px solid transparent;border-bottom:3px solid transparent}
.cta{left:183px;font-size:10.5px;display:flex;align-items:center;gap:5px}

/* sidebar */
.side-h{left:764px;font-size:10.5px}
.sponsor{left:764px;font-family:"Arimo",sans-serif;font-weight:700;color:#1e4f8f;display:flex;align-items:center;gap:5px;white-space:nowrap}
.calendar{left:762px;top:476px;width:188px;height:230px;background:var(--panel);border-radius:3px}
.cal-h{position:absolute;left:10px;top:10px;font-family:"Roboto Condensed",sans-serif;font-size:10.5px;color:var(--red)}
.cal-more{position:absolute;right:10px;top:12px;font-family:"Roboto Condensed",sans-serif;font-size:9px;color:var(--red)}
.event{position:absolute;left:11px;width:167px;font-size:8.3px;color:#444;line-height:10.5px}
.event .date{color:#666;font-size:7.6px;margin-bottom:3px}
.event.rule{border-bottom:1px solid #ccc;padding-bottom:10px}

/* footer */
.footer{left:0;top:980px;width:1150px;height:220px;background:var(--navy)}
.footer-base{left:0;top:1152px;width:1150px;height:48px;background:var(--navy-deep)}
.f-h{font-family:"Roboto Condensed",sans-serif;font-weight:300;font-size:16px;color:#fff}
.f-list{list-style:none;font-size:9px;color:#dfe6ef;line-height:16px}
.affiliate{left:542px;top:1018px;width:142px;height:99px;background:#e9eef5}
.f-social{left:753px;top:1037px;display:flex;gap:8px}
.f-social .sq{width:25px;height:24px}
.legal{left:0;top:1173px;width:1150px;text-align:center;font-size:8px;color:#fff}
</style>
</head>
<body>

<div class="abs topbar"></div>
<div class="abs toplinks"><span>CONTACT US</span><span>SIGN IN</span><span>JOIN/RENEW</span></div>
<div class="abs search">Enter search criteria...
  <svg width="8" height="8" viewBox="0 0 8 8"><circle cx="3.2" cy="3.2" r="2.3" fill="none" stroke="#1a86cc" stroke-width="1.2"/><line x1="5" y1="5" x2="7.5" y2="7.5" stroke="#1a86cc" stroke-width="1.3"/></svg>
</div>
<div class="abs topsocial" aria-label="Social links"><span class="sq"></span><span class="sq"></span><span class="sq"></span><span class="sq"></span><span class="sq"></span></div>

<header class="abs header"></header>
<div class="abs brand"><span class="dot"></span>Metro Workforce Guild</div>
<nav class="abs nav"><span>Our New Website</span><span>About Us</span><span>Membership</span><span>Events</span><span>Sponsorships</span><span>Career Center</span><span>HR Resources</span></nav>
<div class="abs hero" role="img" aria-label="Night skyline of Manhattan with lit office towers"></div>

<main>
  <h1 class="abs title">Invitation for Strategic Partners</h1>
  <div class="abs crumb">Sponsorships &nbsp;» Strategic Partners</div>
  <div class="abs share">
    <span class="mini" style="background:#e2574c"></span>Share <span style="color:#333;margin:0 4px">|</span>
    <span class="mini" style="background:#3b5998"></span><span class="mini" style="background:#1da1f2"></span><span class="mini" style="background:#cb2027"></span><span class="mini" style="background:#d44638"></span>
  </div>
  <p class="abs p" style="top:320px">Thank you for your interest in our strategic partnership.</p>
  <p class="abs p" style="top:344px">Choose the sponsorship package that best meets your needs:</p>

  <div class="abs acc open" style="top:374px">Gold
    <svg width="12" height="12" viewBox="0 0 12 12"><circle cx="6" cy="6" r="6" fill="#fff"/><rect x="3" y="5.2" width="6" height="1.6" fill="#0b7dd3"/></svg></div>
  <div class="abs badge" role="img" aria-label="Strategic Gold Partner badge"></div>
  <p class="abs p" style="top:493px">Thank you for your interest in becoming a Strategic Gold Partner.</p>
  <p class="abs p" style="top:517px">This sponsorship package offers a range of benefits including:</p>
  <ul class="abs benefits">
    <li>3 annual memberships</li><li>1 guest per event</li><li>1 All-Day conference</li>
    <li>4 mini-events</li><li>holiday party</li><li>2 blog posts</li>
  </ul>
  <p class="abs p" style="top:656px">and more</p>

  <div class="abs acc closed" style="top:702px">Silver
    <svg width="12" height="12" viewBox="0 0 12 12"><circle cx="6" cy="6" r="6" fill="#fff"/><rect x="3" y="5.2" width="6" height="1.6" fill="#0a2240"/><rect x="5.2" y="3" width="1.6" height="6" fill="#0a2240"/></svg></div>
  <div class="abs acc closed" style="top:733px">Bronze
    <svg width="12" height="12" viewBox="0 0 12 12"><circle cx="6" cy="6" r="6" fill="#fff"/><rect x="3" y="5.2" width="6" height="1.6" fill="#0a2240"/><rect x="5.2" y="3" width="1.6" height="6" fill="#0a2240"/></svg></div>

  <div class="abs cta" style="top:794px;color:var(--link)">
    <svg width="10" height="9" viewBox="0 0 10 9"><path d="M1 1h8L5 8z" fill="#1a86cc"/></svg>More about our sponsorship packages</div>
  <div class="abs cta" style="top:818px;color:var(--red-link)">
    <svg width="10" height="10" viewBox="0 0 10 10"><rect x="1" y="1" width="8" height="8" rx="1" fill="#c0171d"/></svg>Book your sponsorship package</div>
  <div class="abs cta" style="top:843px">
    <svg width="11" height="8" viewBox="0 0 11 8"><rect width="11" height="8" fill="#333"/><path d="M0 0l5.5 4L11 0" fill="none" stroke="#fff" stroke-width="1"/></svg>Contact our sponsorship team</div>
</main>

<aside>
  <div class="abs side-h" style="top:220px">Thanks to our Sponsors</div>
  <div class="abs side-h" style="top:244px;font-weight:700">Gold</div>
  <div class="abs sponsor" style="top:270px;font-size:18px">Harlan Pierce</div>
  <div class="abs sponsor" style="top:306px;font-size:13px;color:#1f2f6b">TransitPerk Solutions</div>
  <div class="abs side-h" style="top:353px;font-weight:700">Silver</div>
  <div class="abs sponsor" style="top:379px;font-size:15px;color:#222;font-weight:400"><span style="width:9px;height:9px;background:#2a6b2a"></span>Beacon Benefits Group</div>
  <div class="abs sponsor" style="top:412px;font-size:19px;color:#2175d9;font-weight:400">Talentway</div>

  <section class="abs calendar">
    <div class="cal-h">Calendar</div><div class="cal-more">more</div>
    <div class="event rule" style="top:36px"><div class="date">08/16/2016</div>Lorem ipsum dolor sit amet, consectetur adipiscing elit, sed do eiusmod tempor incididunt ut labore et dolore agna aliqua.</div>
    <div class="event rule" style="top:103px"><div class="date">08/16/2016</div>Lorem ipsum dolor sit amet, consectetur adipiscing elit, sed do eiusmod tempor incididunt ut labore et dolore agna aliqua.</div>
    <div class="event" style="top:170px"><div class="date">08/16/2016</div>Lorem ipsum dolor sit amet, consectetur adipiscing elit, sed do eiusmod tempor incididunt ut labore et dolore agna aliqua.</div>
  </section>
</aside>

<footer>
  <div class="abs footer"></div>
  <div class="abs footer-base"></div>
  <div class="abs f-h" style="left:238px;top:1008px">Navigation</div>
  <ul class="abs f-list" style="left:238px;top:1032px">
    <li>About Us</li><li>Membership</li><li>Events</li><li>Career Center</li><li>Sponsorships</li><li>HR Resources</li>
  </ul>
  <div class="abs f-h" style="left:373px;top:1008px">Contact Us</div>
  <ul class="abs f-list" style="left:373px;top:1032px;line-height:23px">
    <li>Phone: 555-014-2290</li><li>Fax: 555-014-2291</li><li>info@metroworkguild.org</li>
  </ul>
  <div class="abs affiliate" role="img" aria-label="Affiliate of National HR Society badge"></div>
  <div class="abs f-h" style="left:753px;top:1008px">Connect With Us</div>
  <div class="abs f-social" aria-label="Social links"><span class="sq"></span><span class="sq"></span><span class="sq"></span><span class="sq"></span><span class="sq"></span></div>
  <div class="abs legal">Membership Software Powered by ClubRoster.com® &nbsp;:: &nbsp;Legal</div>
</footer>

</body>
</html>
```